Melbourne Locksmith Needs a Web Site

We need a web site for our new Locksmith business in Melbourne Australia. Our business is called " Corbett Row Locksmiths" . (Corbett row is a well known in the city and has the famous railway station , it is a main icon of melbourne . Maybe we could incorperate the station maybe in the front page or heading background. our services include Automotive Locksmithing ( Cuting keys to cars, opening cars etc / Master Keys Systems/ Commercial work / Domestic . Also we have no logo yet. but we can get that in the future if needed.

Target Market(s)

(Automotive ) Lost keys to cars, Trucks, Jammed Ignitions, Opening Vehicles. mobile locksmith in a van, Locked out of your house ?

Industry/Entity Type

Business

Number of Pages Required

4 page

Font styles to use
Sans Serif

Colors

Designer to choose colors to be used in the design.

Requirements
Must have
• Phone number easy to read on web site.
Nice to have
• map of where we are, show case pictures of common lock problems for automotive eg ( damaged keys/ Broken).

```html
<!DOCTYPE html>
<html lang="en">
<head>
<meta charset="utf-8">
<title>Corbett Row Locksmiths</title>
<link rel="stylesheet" href="https://fonts.googleapis.com/css2?family=Roboto:wght@400;500;700&family=Open+Sans:ital,wght@0,400;0,600;1,400;1,600&display=swap">
<style>
:root{
  --orange:#e8570e;
  --ink:#2b2b2b;
  --text:#555;
  --muted:#8a8a8a;
  --line:#e3e3e3;
  --dark:#15191f;
  --footer:#f4f4f4;
  --white:#fff;
}
*{margin:0;padding:0;box-sizing:border-box}
html,body{width:1200px;height:2546px;overflow:hidden;background:var(--white)}
body{position:relative;font-family:"Open Sans",Arial,sans-serif;color:var(--text)}
.abs{position:absolute}
a{color:inherit;text-decoration:none}

/* header */
.brand{left:131px;top:38px;font:500 26px/1 "Roboto",sans-serif;color:var(--ink);white-space:nowrap}
.phone{left:828px;top:24px;display:flex;align-items:center;gap:6px;font:400 13px/1 "Roboto",sans-serif;color:#444;white-space:nowrap}
.phone b{font-weight:500;font-size:17px;color:var(--orange)}
.nav{top:67px;left:0;width:1200px;font:500 14px/1 "Roboto",sans-serif;color:#333}
.nav a{position:absolute;white-space:nowrap}
.nav .active{color:var(--orange)}

/* hero */
.hero{left:0;top:109px;width:1200px;height:502px;background:linear-gradient(180deg,#7fb0d8 0%,#a9cbe5 25%,#6c8fa6 45%,#2f6f9c 60%,#1f5f8c 100%)}
.hero-tag{left:436px;top:280px;width:329px;height:54px;background:rgba(30,30,30,.8);color:#fff;font:400 32px/54px "Roboto",sans-serif;text-align:center}
.hero-title{left:232px;top:338px;width:737px;height:69px;background:rgba(30,30,30,.8);color:#fff;font:700 47px/69px "Roboto",sans-serif;text-align:center;white-space:nowrap}
.dot{top:470px;width:20px;height:20px;border-radius:50%;background:#3d5f7a;border:2px solid #fff}
.dot.on{background:var(--orange)}

/* services */
.sec-title{font:500 26px/1 "Roboto",sans-serif;color:var(--ink)}
.services-title{left:0;width:1200px;top:658px;text-align:center}
.services-intro{left:232px;width:736px;top:693px;text-align:center;font-size:11px;line-height:20px;color:#666}
.services-grid{left:132px;top:809px;width:935px;height:192px;border:1px solid var(--line);border-top:4px solid var(--orange);display:flex}
.service{flex:1;border-right:1px solid var(--line);text-align:center;position:relative}
.service:last-child{border-right:none}
.service-icon{position:absolute;left:50%;top:-48px;margin-left:-44px;width:88px;height:88px;border-radius:50%;background:var(--orange);display:flex;align-items:center;justify-content:center}
.service h3{margin-top:60px;font:500 13px/1 "Roboto",sans-serif;color:var(--ink)}
.service p{margin:12px auto 0;width:200px;font-size:11px;line-height:19px;color:#777}
.service .more{display:block;margin-top:12px;font:500 11px/1 "Roboto",sans-serif;color:var(--orange)}

/* about */
.about{left:0;top:1061px;width:1200px;height:427px;background:linear-gradient(180deg,#1b232c 0%,#10151b 70%,#2a2f35 100%)}
.about-title{left:132px;top:1140px;font:500 25px/1 "Roboto",sans-serif;color:#fff}
.about-copy{left:132px;top:1182px;width:430px;font-size:11px;line-height:21px;color:#e6e6e6}
.about-copy p+p{margin-top:10px}
.btn-outline{left:132px;top:1366px;width:124px;height:42px;border:1px solid #ccc;color:#fff;font:500 13px/40px "Roboto",sans-serif;text-align:center}
.video{left:630px;top:1140px;width:437px;height:268px;border:5px solid #fff;background:#fff}
.video-frame{width:100%;height:232px;background:linear-gradient(135deg,#6f8f9c 0%,#a7b6b0 40%,#c9a78a 65%,#4d5a60 100%);position:relative}
.play{position:absolute;left:50%;top:50%;margin:-26px 0 0 -26px;width:52px;height:52px;border-radius:50%;background:rgba(30,30,30,.75);border:2px solid #fff}
.video-bar{height:26px;background:#151515;display:flex;align-items:center;gap:10px;padding:0 10px;font-size:8px;color:#bbb}
.video-bar .track{flex:1;height:3px;background:#555;position:relative}
.video-bar .track i{position:absolute;left:0;top:0;width:80%;height:3px;background:var(--orange)}
.video-bar .vol{width:46px;height:3px;background:#ccc}

/* gallery + testimonials */
.block-title{font:500 19px/1 "Roboto",sans-serif;color:var(--ink)}
.block-rule{height:1px;background:var(--line)}
.block-rule::before{content:"";display:block;width:60px;height:2px;background:var(--orange);margin-top:-1px}
.gallery-nav{left:533px;top:1547px;display:flex;gap:6px}
.gallery-nav span{width:12px;height:12px;border-radius:50%;border:1px solid #999}
.thumb{width:215px;height:150px;border:1px solid var(--line);padding:8px;background:#fff}
.thumb div{width:100%;height:100%}
.quote{left:759px;width:310px;font:italic 400 11px/19px "Open Sans",sans-serif;color:#666}
.quote::before{content:"\201C";position:absolute;left:-16px;top:-12px;font:700 22px/1 Georgia,serif;color:#777}
.quote-end{font:700 22px/1 Georgia,serif;color:#777}
.author{left:859px;width:210px;text-align:right;font:700 12px/1 "Roboto",sans-serif;color:var(--orange)}
.avatar{width:100px;height:100px;border-radius:50%;border:4px solid #e9e9e9;background:linear-gradient(180deg,#cfd7dd,#9aa9b4)}

/* map */
.map{left:0;top:1963px;width:1200px;height:274px;background:linear-gradient(135deg,#e6e2d9 0%,#ece8df 50%,#e2ded4 100%)}
.map-edge{left:0;top:2237px;width:1200px;height:3px;background:var(--orange)}
.location{left:467px;top:2041px;width:237px;height:97px;background:#fff;padding:16px 20px;box-shadow:0 1px 4px rgba(0,0,0,.25)}
.location h4{font:500 12px/1 "Roboto",sans-serif;color:var(--orange);margin-bottom:10px}
.location p{font:500 12px/20px "Roboto",sans-serif;color:#333;white-space:nowrap}

/* footer */
.footer{left:0;top:2240px;width:1200px;height:306px;background:var(--footer)}
.f-head{top:2280px;font:500 14px/1 "Roboto",sans-serif;color:#333}
.f-links{left:132px;top:2317px;font-size:10px;line-height:24px;color:#555;list-style:none}
.f-news{left:321px;top:2305px;width:260px;font-size:10px;line-height:20px;color:#555}
.f-input{left:321px;top:2362px;width:251px;height:39px;border:1px solid #ddd;background:#fff;font-size:10px;line-height:37px;padding-left:16px;color:#555}
.f-btn{left:321px;top:2415px;width:86px;height:34px;background:var(--orange);color:#fff;font:500 11px/34px "Roboto",sans-serif;text-align:center}
.f-contact{left:694px;top:2314px;font-size:10px;color:#555;list-style:none}
.f-contact li{display:flex;gap:12px;height:27px;align-items:flex-start}
.f-contact svg{flex:none;margin-top:2px}
.f-social{left:967px;top:2311px;list-style:none;font-size:10px;color:#555}
.f-social li{display:flex;align-items:center;gap:12px;height:41px}
.f-social span{width:34px;height:34px;border-radius:50%;border:2px solid #333}
.f-rule{left:132px;top:2491px;width:935px;height:1px;background:#ddd}
.copy{left:0;width:1200px;top:2512px;text-align:center;font-size:10px;color:#666}
</style>
</head>
<body>

<header>
  <div class="abs brand">Corbett Row Locksmiths</div>
  <div class="abs phone">
    <svg width="22" height="22" viewBox="0 0 22 22"><circle cx="11" cy="11" r="10" fill="none" stroke="#e8570e" stroke-width="1.6"/><path d="M7.5 6.5c.6-.6 1.3-.4 1.7.2l.9 1.4c.3.5.2 1-.2 1.3l-.6.5c.5 1.3 1.5 2.3 2.8 2.8l.5-.6c.3-.4.8-.5 1.3-.2l1.4.9c.6.4.8 1.1.2 1.7l-.7.7c-.8.8-4.1-.2-6.3-2.4S6 8 6.8 7.2z" fill="#e8570e"/></svg>
    Phone Number : <b>555-014-2290</b>
  </div>
  <nav class="abs nav">
    <a class="active" style="left:460px">Home</a>
    <a style="left:539px">About Us</a>
    <a style="left:637px">Services</a>
    <a style="left:730px">Testimonials</a>
    <a style="left:849px">Gallery</a>
    <a style="left:933px">Blog</a>
    <a style="left:1003px">Contact Us</a>
  </nav>
</header>

<section>
  <div class="abs hero" role="img" aria-label="Photo of the city harbour and skyline on a clear day"></div>
  <div class="abs hero-tag">JAMMED IGNITIONS</div>
  <h1 class="abs hero-title">LOCKED OUT OF YOUR HOUSE ?</h1>
  <span class="abs dot on" style="left:550px"></span>
  <span class="abs dot" style="left:589px"></span>
  <span class="abs dot" style="left:630px"></span>
</section>

<section>
  <h2 class="abs sec-title services-title">Our Services</h2>
  <p class="abs services-intro">Lorem ipsum dolor sit amet, consectetur adipiscing elit, sed do eiusmod tempor incididunt ut labore et dolore magna aliqua. Ut enim ad minim veniam, quis nostrud exercitation ullamco laboris nisi ut aliquip occaecat cupidatat</p>
  <div class="abs services-grid">
    <div class="service">
      <div class="service-icon"><svg width="46" height="46" viewBox="0 0 46 46" fill="#fff"><circle cx="12" cy="9" r="5"/><rect x="16" y="7.5" width="14" height="3"/><rect x="25" y="10" width="2.5" height="4"/><path d="M10 24l3-7h20l3 7h2v11h-4v4h-4v-4H16v4h-4v-4H8V24z"/><circle cx="14" cy="29" r="2.5" fill="#e8570e"/><circle cx="32" cy="29" r="2.5" fill="#e8570e"/></svg></div>
      <h3>Cutting Keys to Cars</h3>
      <p>Excepteur sint occaecat cupidatat non proident, sunt in culpa qui officia deserunt mollit anim...</p>
      <a class="more">Read More &gt;&gt;</a>
    </div>
    <div class="service">
      <div class="service-icon"><svg width="46" height="46" viewBox="0 0 46 46" fill="#fff"><rect x="9" y="20" width="18" height="10" rx="4" transform="rotate(-40 18 25)"/><rect x="22" y="14" width="16" height="4" transform="rotate(-40 30 16)"/><path d="M30 6a9 9 0 0 1 9 9" stroke="#fff" stroke-width="2" fill="none"/><path d="M30 1a14 14 0 0 1 14 14" stroke="#fff" stroke-width="2" fill="none"/></svg></div>
      <h3>Master Keys Systems</h3>
      <p>Excepteur sint occaecat cupidatat non proident, sunt in culpa qui officia deserunt mollit anim...</p>
      <a class="more">Read More &gt;&gt;</a>
    </div>
    <div class="service">
      <div class="service-icon"><svg width="46" height="46" viewBox="0 0 46 46" fill="#fff"><path d="M8 8h30l3 9H5z"/><rect x="8" y="19" width="30" height="20"/><rect x="12" y="23" width="9" height="16" fill="#e8570e"/><rect x="25" y="23" width="9" height="8" fill="#e8570e"/></svg></div>
      <h3>Commercial Work</h3>
      <p>Excepteur sint occaecat cupidatat non proident, sunt in culpa qui officia deserunt mollit anim...</p>
      <a class="more">Read More &gt;&gt;</a>
    </div>
    <div class="service">
      <div class="service-icon"><svg width="46" height="46" viewBox="0 0 46 46" fill="#fff"><path d="M23 5L4 21h5v19h28V21h5z"/><rect x="19" y="28" width="8" height="12" fill="#e8570e"/><rect x="13" y="22" width="6" height="5" fill="#e8570e"/><rect x="27" y="22" width="6" height="5" fill="#e8570e"/></svg></div>
      <h3>Domestic Work</h3>
      <p>Excepteur sint occaecat cupidatat non proident, sunt in culpa qui officia deserunt mollit anim...</p>
      <a class="more">Read More &gt;&gt;</a>
    </div>
  </div>
</section>

<section>
  <div class="abs about" role="img" aria-label="Darkened photo of the city skyline at dusk"></div>
  <h2 class="abs about-title">About Us</h2>
  <div class="abs about-copy">
    <p>Sed ut perspiciatis unde omnis iste natus error sit voluptatem accusantium doloremque laudantium, totam rem aperiam, eaque ipsa quae ab illo inventore veritatis et quasi architecto beatae vitae dicta sunt explicabo. Nemo enim ipsam voluptatem quia voluptas sit aspernatur aut odit aut fugit, sed quia consequuntur</p>
    <p>Sed ut perspiciatis unde omnis iste natus error sit voluptatem accusantium doloremque laudantium, totam rem aperiam, eaque ipsa quae ab illo inventore veritatis et quasi architecto beatae vitae dicta sunt explicabo.</p>
  </div>
  <a class="abs btn-outline">More Videos &nbsp;&#10140;</a>
  <div class="abs video">
    <div class="video-frame" role="img" aria-label="Video still of a driver in a car receiving car keys">
      <span class="play"><svg width="48" height="48" viewBox="0 0 48 48"><path d="M19 15l15 9-15 9z" fill="#fff"/></svg></span>
    </div>
    <div class="video-bar">
      <svg width="8" height="9" viewBox="0 0 8 9"><path d="M0 0l8 4.5L0 9z" fill="#ccc"/></svg>
      <span>00:00/03:03</span>
      <span class="track"><i></i></span>
      <svg width="10" height="9" viewBox="0 0 10 9"><path d="M0 3h3l3-3v9L3 6H0z" fill="#ccc"/></svg>
      <span class="vol"></span>
    </div>
  </div>
</section>

<section>
  <h3 class="abs block-title" style="left:132px;top:1543px">Photo Gallery</h3>
  <div class="abs gallery-nav"><span></span><span></span></div>
  <div class="abs block-rule" style="left:132px;top:1575px;width:433px"></div>
  <div class="abs thumb" style="left:132px;top:1598px"><div role="img" aria-label="Car key with remote in a door lock" style="background:linear-gradient(135deg,#d9d9d9,#8e8e8e)"></div></div>
  <div class="abs thumb" style="left:352px;top:1598px"><div role="img" aria-label="Key cutting machine at work" style="background:linear-gradient(135deg,#3c6e9a,#c8683a)"></div></div>
  <div class="abs thumb" style="left:132px;top:1756px"><div role="img" aria-label="Keys in a car ignition" style="background:linear-gradient(135deg,#1b2430,#4a5562)"></div></div>
  <div class="abs thumb" style="left:352px;top:1756px"><div role="img" aria-label="Silver key on a dark blue background" style="background:linear-gradient(135deg,#1e3550,#2c4a6a)"></div></div>

  <h3 class="abs block-title" style="left:631px;top:1543px">Testimonials</h3>
  <div class="abs block-rule" style="left:631px;top:1575px;width:436px"></div>

  <div class="abs avatar" role="img" aria-label="Customer portrait" style="left:636px;top:1598px"></div>
  <p class="abs quote" style="top:1619px">Nulla sollicitudin tincidunt dui et egestas. Phasellus non sem tum, ullamcorper vitae, accumsan dui. Duis dignissim condi lorem. Maecenas facilisis ipsum sed . <span class="quote-end">&#8221;</span></p>
  <div class="abs author" style="top:1701px">-MARCUS TOLLEY</div>
  <div class="abs" style="left:631px;top:1744px;width:436px;height:1px;background:var(--line)"></div>

  <div class="abs avatar" role="img" aria-label="Customer portrait" style="left:636px;top:1793px"></div>
  <p class="abs quote" style="top:1810px">Nulla sollicitudin tincidunt dui et egestas. Phasellus non sem tum, ullamcorper vitae, accumsan dui. Duis dignissim condi lorem. Maecenas facilisis ipsum sed . <span class="quote-end">&#8221;</span></p>
  <div class="abs author" style="top:1892px">-MARCUS TOLLEY</div>
</section>

<section>
  <div class="abs map" role="img" aria-label="Street map around the shop location"></div>
  <div class="abs location">
    <h4>OUR LOCATION</h4>
    <p>423# Corbett Row Locksmiths<br>Street Name,City-67645</p>
  </div>
  <svg class="abs" style="left:752px;top:2074px" width="20" height="30" viewBox="0 0 20 30"><path d="M10 0a10 10 0 0 1 10 10c0 7-10 20-10 20S0 17 0 10A10 10 0 0 1 10 0z" fill="#e0392a"/><circle cx="10" cy="10" r="3.5" fill="#8e1d14"/></svg>
  <div class="abs map-edge"></div>
</section>

<footer>
  <div class="abs footer"></div>
  <h4 class="abs f-head" style="left:132px">Quick Links</h4>
  <ul class="abs f-links">
    <li>Home</li><li>About Us</li><li>Services</li><li>Testimonials</li><li>Blog</li><li>Contact us</li>
  </ul>

  <h4 class="abs f-head" style="left:321px">Newsletter</h4>
  <p class="abs f-news">Enter your email address to receive the latest news and notes from our blog.</p>
  <div class="abs f-input">Enter Your Mail Id</div>
  <div class="abs f-btn">Subscribe</div>

  <h4 class="abs f-head" style="left:694px">Contact Info</h4>
  <ul class="abs f-contact">
    <li><svg width="12" height="10" viewBox="0 0 12 10"><path d="M1 2c3-2 7-2 10 0v2H8V3H4v1H1zM3 5h6l2 4H1z" fill="#555"/></svg>(555) 016-4410</li>
    <li><svg width="12" height="10" viewBox="0 0 12 10"><rect x="3" y="0" width="6" height="3" fill="#555"/><rect x="0" y="3" width="12" height="5" fill="#555"/><rect x="3" y="6" width="6" height="4" fill="#fff" stroke="#555"/></svg>(555) 016-4410</li>
    <li><svg width="12" height="10" viewBox="0 0 12 10"><rect x="0" y="1" width="12" height="8" fill="#555"/><path d="M0 1l6 4 6-4" stroke="#fff" fill="none"/></svg><u>hello@corbettrowlocks.example</u></li>
    <li style="line-height:15px"><svg width="12" height="12" viewBox="0 0 12 12"><path d="M6 0a4 4 0 0 1 4 4c0 3-4 8-4 8S2 7 2 4a4 4 0 0 1 4-4z" fill="#555"/></svg>#2868 Lorem ipsum dolor sit<br>amet, consectetur</li>
  </ul>

  <h4 class="abs f-head" style="left:967px">Follow Us</h4>
  <ul class="abs f-social">
    <li><span></span>Socialnet</li>
    <li><span></span>Chirpline</li>
    <li><span></span>Circleup</li>
    <li><span></span>Worklink</li>
  </ul>

  <div class="abs f-rule"></div>
  <p class="abs copy">&copy;2017 Corbett Row Locksmiths | all rights reserved</p>
</footer>

</body>
</html>
```